Banner Project for website

We do not like our current banner and need this updated. Our website is:
https://inkvelmo.com/
We need the banner to have the following wording on the left side:
See attachment. (screenshot text on the left)
On the right side, I want to replace the lady and have a nice image of printed products like the following websites which have an image with different printed prodcuts bundled together or seperately.
https://www.labelwharf.com/
https://boxtiderun.com/
The banner must look fresh and vibrant
Target Market(s)
Small businesses
Industry/Entity Type
Printing
Requirements
Must have
- Greta banner image

```html
<!DOCTYPE html>
<html lang="en">
<head>
<meta charset="utf-8">
<title>Inkvelmo – Compare Quotes and Save</title>
<link href="https://fonts.googleapis.com/css2?family=Poppins:wght@400;500;600;700;800&display=swap" rel="stylesheet">
<style>
  :root {
    --page-bg: #e3e3e3;
    --navy-deep: #0a3565;
    --navy: #074a85;
    --navy-light: #0b5896;
    --gold: #ffd03a;
    --amber: #ffa21a;
    --orange: #ff8800;
    --white: #ffffff;
    --ink: #1d1d1d;
    --teal: #17a5c2;
  }
  * { box-sizing: border-box; margin: 0; padding: 0; }
  html, body {
    width: 1200px; height: 858px; overflow: hidden;
    background: var(--page-bg);
    font-family: "Poppins", sans-serif;
  }
  .banner {
    position: absolute; left: 101px; top: 210px;
    width: 999px; height: 438px; overflow: hidden;
    background: linear-gradient(120deg, var(--navy-deep) 0%, var(--navy) 55%, var(--navy-light) 100%);
    box-shadow: 0 2px 6px rgba(0,0,0,0.25);
  }
  .banner-copy { position: absolute; left: 48px; top: 40px; width: 520px; }
  .headline {
    font-weight: 800; font-size: 50px; line-height: 48px; letter-spacing: -0.5px;
    background: linear-gradient(180deg, var(--gold) 0%, var(--amber) 100%);
    -webkit-background-clip: text; background-clip: text; color: transparent;
  }
  .intro {
    margin-top: 18px; color: var(--white);
    font-size: 20.5px; line-height: 26px; font-weight: 400; letter-spacing: -0.2px;
  }
  .tagline {
    margin-top: 12px; color: var(--gold);
    font-size: 19px; font-weight: 700; letter-spacing: -0.4px;
  }
  .quote-form { position: absolute; left: 46px; top: 270px; width: 357px; }
  .field {
    height: 35px; background: var(--white); border-radius: 6px;
    display: flex; align-items: center; padding-left: 14px;
    color: var(--ink); font-size: 17px; font-weight: 500; margin-bottom: 9px;
  }
  .field-sub { padding-left: 19px; }
  .get-quotes {
    height: 35px; border-radius: 6px; border: none; width: 100%;
    background: linear-gradient(90deg, var(--orange) 0%, var(--gold) 100%);
    color: var(--ink); font-family: "Poppins", sans-serif;
    font-size: 17px; font-weight: 600;
  }
  .product-mosaic { position: absolute; left: 0; top: 0; }
</style>
</head>
<body>
  <section class="banner">
    <svg class="product-mosaic" width="999" height="438" viewBox="0 0 999 438">
      <defs>
        <linearGradient id="tile-gold" x1="0" y1="0" x2="1" y2="1">
          <stop offset="0" stop-color="#ffc23a"/><stop offset="1" stop-color="#ff8c00"/>
        </linearGradient>
      </defs>
      <circle class="ring" cx="1010" cy="70" r="70" fill="none" stroke="#2a6aa8" stroke-width="2" opacity="0.6"/>
      <circle class="ring" cx="700" cy="330" r="60" fill="none" stroke="#2a6aa8" stroke-width="2" opacity="0.4"/>

      <polygon role="img" aria-label="Photo of a printed wall sticker and cafe posters" points="697,0 822,0 795,66 687,66" fill="#9fd6d8"/>
      <polygon role="img" aria-label="Photo of a round holographic sticker on a hoodie" points="831,0 959,0 931,120 811,120" fill="#8a8f9a"/>
      <polygon role="img" aria-label="Photo of printed business cards with a paper clip" points="603,77 727,77 703,201 579,201" fill="#e6ebea"/>
      <polygon role="img" aria-label="Photo of a printed real estate calendar magnet" points="729,130 853,130 829,254 705,254" fill="var(--teal)"/>
      <polygon role="img" aria-label="Photo of a stack of round printed vote stickers" points="855,189 977,189 953,312 829,312" fill="#f4f4f6"/>
      <polygon role="img" aria-label="Photo of round orange printed cafe stickers" points="634,262 759,262 735,387 610,387" fill="#f39a3c"/>
      <polygon role="img" aria-label="Photo of a printed vinyl banner on a barrier fence" points="757,331 883,331 863,438 735,438" fill="#c9cccf"/>

      <g class="accent-square">
        <polygon points="623,16 670,16 662,62 615,62" fill="url(#tile-gold)"/>
        <polygon points="637,34 680,34 673,71 630,71" fill="none" stroke="#fff" stroke-width="3"/>
      </g>
      <g class="accent-square">
        <polygon points="859,129 904,129 896,173 851,173" fill="url(#tile-gold)"/>
        <polygon points="873,146 915,146 908,182 866,182" fill="none" stroke="#fff" stroke-width="3"/>
      </g>
      <g class="accent-square">
        <polygon points="762,268 808,268 800,313 754,313" fill="url(#tile-gold)"/>
        <polygon points="776,286 818,286 811,322 769,322" fill="none" stroke="#fff" stroke-width="3"/>
      </g>
      <g class="accent-frame">
        <polygon points="765,77 808,77 799,120 756,120" fill="#fff"/>
        <polygon points="776,89 808,89 801,120 770,120" fill="var(--navy)"/>
      </g>
      <g class="accent-frame">
        <polygon points="657,209 700,209 691,253 648,253" fill="#fff"/>
        <polygon points="668,221 700,221 693,253 662,253" fill="var(--navy)"/>
      </g>
      <g class="accent-frame">
        <polygon points="897,322 940,322 931,366 888,366" fill="#fff"/>
        <polygon points="908,334 940,334 933,366 902,366" fill="var(--navy)"/>
      </g>
    </svg>

    <div class="banner-copy">
      <h1 class="headline">COMPARE QUOTES<br>AND SAVE</h1>
      <p class="intro">Get instant quotes, compare products from multiple printers and get the best price</p>
      <p class="tagline">EASY ONLINE ORDERING AND FREE DESIGN</p>
    </div>

    <form class="quote-form">
      <div class="field">What do you want to print today?</div>
      <div class="field field-sub">Sub Category</div>
      <button class="get-quotes" type="button">GET QUOTES</button>
    </form>
  </section>
</body>
</html>
```